Lift Her Summit - Marketing Graphic Needed

Non-profit needs a full page and header size graphic for our 2023 Lift Her Summit.

The theme this year is: Unrestrained
Date: January 27, 2023
Location: Harborlight Stays Meeting Hall | San Marcos, TX
Focus (not to be included on flyer): identifying what's holding us back; moving forward; practice makes progress; creating new paradigms; dispelling self-sabotage; clarifying goals; how to kick butt and play to win; being true to your self; building self-confidence; working less to get more.

Target Market(s)

Women in the design and construction industry (architects, engineers, project managers, project Owners, attorneys)

Industry/Entity Type

Design and Construction

Requirements
Must have
• Title of Forum, Theme, date, location, Q-BraTM logo and Lift Her logo
Nice to have
• a graphic that exemplifies the theme: "Unrestrained"

```html
<!DOCTYPE html>
<html lang="en">
<head>
<meta charset="utf-8">
<title>Unrestrained 2023 – Lift Her Summit</title>
<link rel="stylesheet" href="https://fonts.googleapis.com/css2?family=Kaushan+Script&family=Comfortaa:wght@400;700&family=Nunito:wght@400;700;800&family=Roboto:wght@400&family=Roboto+Condensed:ital,wght@0,700;1,700&display=swap">
<style>
  :root {
    --backdrop: #4b4b4b;
    --royal: #1f3f94;
    --footer-blue: #25409a;
    --lime: #b8e21a;
    --leaf: #7fb23a;
    --white: #ffffff;
    --ink-grey: #555a60;
    --soft-grey: #8a8f95;
    --line-grey: #c9ccd0;
    --nav-blue: #1f5e9c;
    --accent-blue: #3ba7e8;
    --mission-orange: #d9822b;
    --footer-text: #c9cff0;
    --photo-sky: #cfdbe6;
    --photo-mid: #9fb0bf;
    --photo-dark: #3a3f48;
    --dusk-top: #f2b07a;
    --dusk-mid: #6c6f86;
    --dusk-low: #2c3a46;
  }
  * { margin: 0; padding: 0; box-sizing: border-box; }
  html, body { width: 1200px; height: 2178px; overflow: hidden; }
  body {
    position: relative;
    background: var(--white);
    font-family: "Nunito", sans-serif;
  }

  /* ---------- stage behind the hero banner ---------- */
  .stage {
    position: absolute;
    left: 0; top: 0;
    width: 1200px; height: 782px;
    background: var(--backdrop);
  }

  /* ---------- event banner (built at 1100 × 618, scaled per use) ---------- */
  .banner {
    position: absolute;
    width: 1100px;
    height: 618px;
    background: var(--royal);
    overflow: hidden;
    transform-origin: 0 0;
  }
  .banner--hero { left: 81px; top: 106px; transform: scale(0.9427); }
  .banner--page { left: 23px; top: 1404px; transform: scale(1.0527); }

  .banner__photo {
    position: absolute;
    inset: 0;
    background: linear-gradient(160deg, var(--photo-sky) 30%, var(--photo-mid) 60%, var(--photo-dark) 95%);
    clip-path: polygon(811px 0, 1100px 0, 1100px 618px, 299px 618px);
  }
  .banner__theme {
    position: absolute;
    left: 44px; top: 40px;
    font-family: "Kaushan Script", cursive;
    font-size: 84px;
    line-height: 1;
    color: var(--lime);
  }
  .banner__year {
    position: absolute;
    left: 40px; top: 132px;
    font-family: "Comfortaa", sans-serif;
    font-weight: 700;
    font-size: 164px;
    line-height: 1;
    letter-spacing: 2px;
    color: var(--lime);
  }
  .banner__rule {
    position: absolute;
    left: 49px; top: 284px;
    width: 392px; height: 3px;
    background: var(--lime);
  }
  .banner__title {
    position: absolute;
    left: 53px; top: 302px;
    font-weight: 800;
    font-size: 29px;
    color: var(--white);
  }
  .banner__date {
    position: absolute;
    left: 56px; top: 351px;
    font-family: "Comfortaa", sans-serif;
    font-weight: 400;
    font-size: 33px;
    color: var(--white);
  }
  .banner__venue {
    position: absolute;
    left: 52px; top: 398px;
    display: flex;
    align-items: center;
    gap: 6px;
    font-weight: 800;
    font-size: 14.5px;
    color: var(--white);
  }
  .banner__venue svg { width: 16px; height: 18px; }
  .banner__org {
    position: absolute;
    left: 57px; top: 473px;
    display: flex;
    align-items: center;
    gap: 18px;
  }
  .banner__org-dot {
    width: 74px; height: 74px;
    border-radius: 50%;
    background: var(--white);
  }
  .banner__org-name {
    font-weight: 800;
    font-size: 37px;
    line-height: 1;
    color: var(--white);
  }
  .banner__org-tagline {
    margin-top: 6px;
    font-weight: 700;
    font-size: 8.5px;
    color: var(--lime);
  }

  /* ---------- website header ---------- */
  .site-brand {
    position: absolute;
    left: 15px; top: 808px;
    display: flex;
    align-items: center;
    gap: 16px;
  }
  .site-brand__dot {
    width: 104px; height: 104px;
    border-radius: 50%;
    background: var(--royal);
  }
  .site-brand__name {
    font-weight: 800;
    font-size: 54px;
    line-height: 1;
    color: var(--ink-grey);
    padding-bottom: 6px;
    border-bottom: 2px solid var(--ink-grey);
  }
  .site-brand__tagline {
    margin-top: 10px;
    font-weight: 400;
    font-size: 12.5px;
    color: var(--leaf);
  }
  .site-login {
    position: absolute;
    right: 13px; top: 810px;
    font-size: 16px;
    color: var(--soft-grey);
  }
  .site-search {
    position: absolute;
    left: 914px; top: 873px;
    width: 274px; height: 33px;
    border: 1px solid var(--line-grey);
    display: flex;
    align-items: center;
    gap: 8px;
    padding-left: 8px;
    font-family: "Nunito", sans-serif;
    font-size: 17px;
    color: var(--soft-grey);
  }
  .site-search svg { width: 16px; height: 16px; }

  .site-nav {
    position: absolute;
    left: 14px; top: 989px;
    width: 1174px; height: 49px;
    border-bottom: 5px solid var(--nav-blue);
    font-family: "Roboto", sans-serif;
    font-size: 19px;
    color: var(--ink-grey);
  }
  .site-nav__item {
    position: absolute;
    top: 0;
    line-height: 26px;
    white-space: nowrap;
  }
  .site-nav__item--sub::after {
    content: "";
    display: inline-block;
    width: 6px; height: 6px;
    margin-left: 11px;
    vertical-align: middle;
    border-radius: 50%;
    background: var(--accent-blue);
  }
  .site-nav__item--active::before {
    content: "";
    position: absolute;
    left: 0; top: 37px;
    width: 60px; height: 5px;
    background: var(--accent-blue);
  }
  .site-nav__menu {
    position: absolute;
    left: 1146px; top: 4px;
    width: 22px; height: 18px;
    border-top: 3px solid var(--ink-grey);
    border-bottom: 3px solid var(--ink-grey);
  }
  .site-nav__menu::after {
    content: "";
    position: absolute;
    left: 0; top: 4.5px;
    width: 22px; height: 3px;
    background: var(--ink-grey);
  }

  /* ---------- mission strip ---------- */
  .mission {
    position: absolute;
    left: 14px; top: 1040px;
    width: 1174px; height: 343px;
    background: linear-gradient(180deg, var(--dusk-top) 0%, var(--dusk-mid) 32%, var(--dusk-low) 75%);
  }
  .mission__label {
    position: absolute;
    left: 13px; top: 61px;
    font-family: "Roboto Condensed", sans-serif;
    font-weight: 700;
    font-size: 24px;
    color: var(--mission-orange);
  }
  .mission__text {
    position: absolute;
    left: 13px; top: 117px;
    width: 620px;
    font-family: "Roboto Condensed", sans-serif;
    font-style: italic;
    font-weight: 700;
    font-size: 20.5px;
    line-height: 27px;
    color: var(--white);
  }

  /* ---------- footer bar ---------- */
  .site-footer {
    position: absolute;
    left: 15px; top: 2074px;
    width: 1173px; height: 59px;
    background: var(--footer-blue);
  }
  .site-footer__social {
    position: absolute;
    top: 17px;
    width: 26px; height: 26px;
    border-radius: 50%;
    border: 2.5px solid var(--footer-text);
  }
  .site-footer__web {
    position: absolute;
    left: 672px; top: 0;
    height: 59px;
    display: flex;
    align-items: center;
    gap: 22px;
    font-family: "Nunito", sans-serif;
    font-weight: 700;
    font-size: 17px;
    color: var(--footer-text);
  }
  .site-footer__web svg { width: 26px; height: 26px; }
</style>
</head>
<body>
  <div class="stage"></div>

  <section class="banner banner--hero">
    <div class="banner__photo" role="img" aria-label="Photo of a smiling woman in a blue hard hat and black blazer on a phone, in front of an industrial plant, with a breaking steel chain along the diagonal edge"></div>
    <div class="banner__theme">Unrestrained</div>
    <div class="banner__year">2023</div>
    <div class="banner__rule"></div>
    <h1 class="banner__title">Lift Her Summit</h1>
    <p class="banner__date">January 27, 2023</p>
    <p class="banner__venue">
      <svg viewBox="0 0 16 18" aria-hidden="true"><path d="M8 1a5 5 0 0 0-5 5c0 3.6 5 8.5 5 8.5s5-4.9 5-8.5a5 5 0 0 0-5-5z" fill="none" stroke="#fff" stroke-width="1.6"/><circle cx="8" cy="6" r="1.8" fill="#fff"/><ellipse cx="8" cy="16" rx="6" ry="1.4" fill="none" stroke="#fff" stroke-width="1.2"/></svg>
      Harborlight Stays Meeting Hall | San Marcos, TX
    </p>
    <div class="banner__org">
      <div class="banner__org-dot"></div>
      <div>
        <div class="banner__org-name">Q-BraTM</div>
        <div class="banner__org-tagline">Quorum for Builders in Team Management</div>
      </div>
    </div>
  </section>

  <header>
    <div class="site-brand">
      <div class="site-brand__dot"></div>
      <div>
        <div class="site-brand__name">Q-BraTM</div>
        <div class="site-brand__tagline">Quorum for Builders in Team Management</div>
      </div>
    </div>
    <div class="site-login">Log in</div>
    <div class="site-search">
      <svg viewBox="0 0 16 16" aria-hidden="true"><circle cx="6.5" cy="6.5" r="5" fill="none" stroke="#333" stroke-width="2"/><line x1="10.2" y1="10.2" x2="15" y2="15" stroke="#333" stroke-width="2.4"/></svg>
      Search
    </div>
    <nav class="site-nav">
      <span class="site-nav__item site-nav__item--active" style="left:0">HOME</span>
      <span class="site-nav__item site-nav__item--sub" style="left:99px">BLUEBONNET GREEN BUILD FORUM</span>
      <span class="site-nav__item site-nav__item--sub" style="left:537px">ABOUT US</span>
      <span class="site-nav__item site-nav__item--sub" style="left:686px">MEMBERSHIP</span>
      <span class="site-nav__item site-nav__item--sub" style="left:867px">EVENTS</span>
      <span class="site-nav__item site-nav__item--sub" style="left:987px">CHAPTERS</span>
      <span class="site-nav__menu"></span>
    </nav>
  </header>

  <section class="mission" role="img" aria-label="Aerial photo of a city skyline and river at dusk">
    <h2 class="mission__label">OUR MISSION</h2>
    <p class="mission__text">Evolve the capital projects industry though sharing of knowledge for optimized leadership, delivery and performance.</p>
  </section>

  <section class="banner banner--page">
    <div class="banner__photo" role="img" aria-label="Photo of a smiling woman in a blue hard hat and black blazer on a phone, in front of an industrial plant, with a breaking steel chain along the diagonal edge"></div>
    <div class="banner__theme">Unrestrained</div>
    <div class="banner__year">2023</div>
    <div class="banner__rule"></div>
    <h2 class="banner__title">Lift Her Summit</h2>
    <p class="banner__date">January 27, 2023</p>
    <p class="banner__venue">
      <svg viewBox="0 0 16 18" aria-hidden="true"><path d="M8 1a5 5 0 0 0-5 5c0 3.6 5 8.5 5 8.5s5-4.9 5-8.5a5 5 0 0 0-5-5z" fill="none" stroke="#fff" stroke-width="1.6"/><circle cx="8" cy="6" r="1.8" fill="#fff"/><ellipse cx="8" cy="16" rx="6" ry="1.4" fill="none" stroke="#fff" stroke-width="1.2"/></svg>
      Harborlight Stays Meeting Hall | San Marcos, TX
    </p>
    <div class="banner__org">
      <div class="banner__org-dot"></div>
      <div>
        <div class="banner__org-name">Q-BraTM</div>
        <div class="banner__org-tagline">Quorum for Builders in Team Management</div>
      </div>
    </div>
  </section>

  <footer class="site-footer">
    <span class="site-footer__social" style="left:53px"></span>
    <span class="site-footer__social" style="left:109px"></span>
    <span class="site-footer__social" style="left:165px"></span>
    <div class="site-footer__web">
      <svg viewBox="0 0 26 26" aria-hidden="true"><circle cx="13" cy="13" r="10.5" fill="none" stroke="#c9cff0" stroke-width="2.2"/><ellipse cx="13" cy="13" rx="4.5" ry="10.5" fill="none" stroke="#c9cff0" stroke-width="1.8"/><line x1="2.5" y1="13" x2="23.5" y2="13" stroke="#c9cff0" stroke-width="1.8"/></svg>
      Q-BraTM.org
    </div>
  </footer>
</body>
</html>
```